Learning Horizon Collective Website

Background

Learning Horizon Collective (LHC) is a newly established consultancy that focuses on education, primarily improving schools and universities. The company is registered in Dubai.

Domain name is learnhorizonco.com, the logo for LHC is attached as is the registered business address

Scope

LHC requests designers to design and build a website that initially includes the following key pages/sections.

• About us/our story
• Our people
• Our services
• Our work
• Contact us/social media

Some examples of websites that are similar to the look and feel of a new contemporary startup like LHC include the following:
http://www.telvano.co/journal/
https://www.quorimadvisory.com/

Content to be provided by LHC. In addition, LHC wishes the successful designer to set up all email and social media accounts required.

Target Market(s)

Government Education departments, donors, Private school chains, school owners, NGOs, investors

Industry/Entity Type

Education

Number of Pages Required

3 page

Font styles to use
Sans Serif

Colors

Designer to choose colors to be used in the design.

Requirements
Must have
• • About us/our story
• • Our people
• • Our services
• • Our work
• • Contact us/social media
• (Maximum 3 pages)
• domain name, address, our services etc
• Blend colours with logo design colours
Nice to have
• Given the migration to mobile devices, we think that having a site which can be scrolled from top to bottom would be preferable
• Possibly a lite version in areas where bandwidth is poor?
Should not have
• Anything that takes a long time to download

```html
<!DOCTYPE html>
<html lang="en">
<head>
<meta charset="utf-8">
<title>Learning Horizon Collective</title>
<link href="https://fonts.googleapis.com/css2?family=Arimo:wght@400;700&family=Raleway:wght@400;500;600;700&display=swap" rel="stylesheet">
<style>
:root{
  --navy:#1d3f7a;
  --band:#384a92;
  --nav:#2f4592;
  --circle:#0d4f95;
  --footer:#1f3a70;
  --footer-base:#142a52;
  --teal:#2f9fc8;
  --cyan:#46b8e0;
  --white:#ffffff;
  --muted:#c9c9c9;
}
*{margin:0;padding:0;box-sizing:border-box}
html,body{width:1200px;height:1200px;overflow:hidden;background:var(--white)}
.page{position:absolute;left:0;top:0;width:1500px;height:1500px;transform:scale(.8);transform-origin:0 0;font-family:"Arimo",Arial,sans-serif}
.abs{position:absolute}
.header{left:352px;top:0;width:798px;height:144px;background:linear-gradient(90deg,#fff 0%,#fff 28%,#a9b1d2 52%,#5564a2 70%,#3b4a93 100%);border-top:3px solid #2a3c7e}
.address-tab{left:625px;top:0;width:453px;height:32px;background:#3b4a93;border-radius:0 0 10px 10px;color:#fff;font-size:9.5px;line-height:34px;text-align:center}
.brand{left:372px;top:36px;color:#2a3c8c;font-family:"Raleway",sans-serif;font-weight:700;font-size:30px;line-height:33px;width:320px}
.search{left:877px;top:62px;width:178px;height:25px;background:#fff;border-radius:4px 0 0 4px}
.search-btn{left:1055px;top:62px;width:26px;height:26px;background:var(--navy)}
.nav{left:620px;top:115px;height:27px;display:flex;background:var(--nav);border-right:1px solid #8ea0d8}
.nav span{color:#fff;font-size:10px;line-height:27px;border-left:1px solid #8ea0d8;padding:0 8px;display:flex;align-items:center;justify-content:space-between}
.nav i{display:inline-block;width:7px;height:7px;border-radius:50%;background:#fff;margin-left:6px}
.hero{left:352px;top:144px;width:798px;height:267px;background:linear-gradient(180deg,#1f5fb0 0%,#5a9ad6 35%,#8aa6a0 48%,#2a7f9a 62%,#156b8c 100%)}
.services{left:352px;top:411px;width:798px;height:193px;background:var(--band);color:#fff;text-align:center}
.services h2{font-weight:400;font-size:20px;margin-top:30px}
.services p{font-size:11px;letter-spacing:.6px;margin-top:13px}
.card{left:421px;top:525px;width:661px;height:149px;background:#fff;box-shadow:0 1px 4px rgba(0,0,0,.35)}
.svc-icon{top:552px;width:82px;height:82px}
.svc-name{top:641px;width:160px;text-align:center;font-family:"Raleway",sans-serif;font-weight:600;font-size:11px;letter-spacing:.6px;color:var(--navy)}
.btn-other{left:965px;top:663px;width:111px;height:26px;background:var(--navy);color:#fff;font-size:10px;line-height:26px;text-align:center;border:1px solid #2d5aa8}
.placeholder{left:433px;top:710px;width:341px;height:259px;border:2px solid #111;display:flex;align-items:center;justify-content:center;text-align:center;font-family:"Raleway",sans-serif;font-weight:700;font-size:33px;line-height:40px;color:var(--muted)}
.about{left:827px;top:738px;width:258px;font-family:"Raleway",sans-serif}
.about h3,.work-title{font-family:"Raleway",sans-serif;font-weight:600;font-size:21px;letter-spacing:1.2px;color:var(--navy)}
.about p{font-size:9.6px;line-height:17.8px;letter-spacing:.6px;color:var(--teal);margin-top:6px}
.countries{display:grid;grid-template-columns:93px 88px 74px;margin-top:4px;font-size:9.6px;line-height:17.8px;letter-spacing:.6px;color:var(--teal)}
.btn-read{left:829px;top:944px;width:83px;height:28px;border:1px solid #7a8fb8;border-left:4px solid var(--navy);font-family:"Raleway",sans-serif;font-size:10px;letter-spacing:.5px;line-height:26px;text-align:center;color:#333;background:#fff}
.work-title{left:421px;top:990px}
.work{left:420px;top:1020px;width:666px;height:142px;background:var(--band);padding:8px 14px;font-family:"Raleway",sans-serif;font-size:9.6px;line-height:17.8px;letter-spacing:.6px;color:var(--cyan)}
.work p{width:575px}
.btn-work{left:434px;top:1119px;width:83px;height:28px;border:1px solid #fff;border-left:4px solid #fff;color:#fff;font-family:"Raleway",sans-serif;font-size:10px;line-height:26px;text-align:center}
.footer{left:352px;top:1221px;width:798px;height:229px;background:var(--footer);border-top:3px solid #2a55a0;color:#fff}
.footer h4{position:absolute;font-family:"Raleway",sans-serif;font-weight:500;font-size:20px;top:10px}
.footer ul{position:absolute;list-style:none;left:68px;top:46px;font-size:10.5px;line-height:17.8px}
.footer .addr{position:absolute;left:350px;top:37px;font-size:10.5px;line-height:17.8px}
.btn-contact{position:absolute;left:633px;top:46px;width:83px;height:28px;border:1px solid #fff;border-left:4px solid #fff;font-size:10px;line-height:26px;text-align:center;background:var(--band)}
.base{left:352px;top:1450px;width:798px;height:50px;background:var(--footer-base);color:#fff;font-size:9px}
.base span{position:absolute;top:24px}
</style>
</head>
<body>
<div class="page">
  <header class="abs header"></header>
  <div class="abs address-tab">Business Center, Marwan Crest Building, Harbor Free Zone, Qasr Al Noor, U.A.E.</div>
  <div class="abs brand">Learning Horizon<br>Collective</div>
  <div class="abs search"></div>
  <div class="abs search-btn">
    <svg width="26" height="26" viewBox="0 0 26 26"><circle cx="12" cy="11" r="5" fill="none" stroke="#fff" stroke-width="2"/><line x1="15.5" y1="14.5" x2="20" y2="19" stroke="#fff" stroke-width="2.5"/></svg>
  </div>
  <nav class="abs nav">
    <span style="width:80px">ABOUT US</span>
    <span style="width:80px">SERVICES<i></i></span>
    <span style="width:100px">Our People<i></i></span>
    <span style="width:94px">Our Work<i></i></span>
    <span style="width:107px;padding-left:15px">CONTACT US</span>
  </nav>
  <div class="abs hero" role="img" aria-label="Panoramic photo of a harbour city skyline with opera house and blue water"></div>

  <section class="abs services">
    <h2>SERVICES</h2>
    <p>We provide following services</p>
  </section>
  <div class="abs card"></div>
  <svg class="abs svc-icon" style="left:473px" viewBox="0 0 82 82"><circle cx="41" cy="41" r="41" fill="var(--circle)"/><path d="M14 37 L41 27 L68 37 L41 47 Z" fill="#fff"/><path d="M26 43 V54 Q41 62 56 54 V43 L41 49 Z" fill="#fff"/><line x1="18" y1="39" x2="18" y2="56" stroke="#fff" stroke-width="2"/></svg>
  <svg class="abs svc-icon" style="left:694px" viewBox="0 0 82 82"><circle cx="41" cy="41" r="41" fill="var(--circle)"/><path d="M14 37 L41 27 L68 37 L41 47 Z" fill="#fff"/><path d="M26 43 V54 Q41 62 56 54 V43 L41 49 Z" fill="#fff"/><line x1="18" y1="39" x2="18" y2="56" stroke="#fff" stroke-width="2"/></svg>
  <svg class="abs svc-icon" style="left:917px" viewBox="0 0 82 82"><circle cx="41" cy="41" r="41" fill="var(--circle)"/><path d="M14 37 L41 27 L68 37 L41 47 Z" fill="#fff"/><path d="M26 43 V54 Q41 62 56 54 V43 L41 49 Z" fill="#fff"/><line x1="18" y1="39" x2="18" y2="56" stroke="#fff" stroke-width="2"/></svg>
  <div class="abs svc-name" style="left:434px">School Improvement</div>
  <div class="abs svc-name" style="left:655px">University Reform</div>
  <div class="abs svc-name" style="left:878px">System Advisory</div>
  <div class="abs btn-other">OTHER SERVICES</div>

  <div class="abs placeholder">Image<br>Coming<br>Soon</div>
  <section class="abs about">
    <h3>About Us</h3>
    <p>The Partners have extensive international educational consultancy experience and have worked extensively improving schools, universities, education systems with delivery in the following countries:</p>
    <div class="countries">
      <span>United Kingdom</span><span>United States</span><span>Pakistan</span>
      <span>Australi</span><span>Bahrain</span><span>India,</span>
      <span>Germany</span><span>U.A.E</span><span>South&nbsp; Africa</span>
      <span>Saudi Arabia</span><span>Jordan</span><span></span>
    </div>
  </section>
  <div class="abs btn-read">Read More</div>

  <h3 class="abs work-title">Our Work</h3>
  <section class="abs work">
    <p>The Partners have extensive experience in large-scale education reform across the K-12 and higher education sectors. These experiences have included work within advanced and emerging economy countries, as well systems with more than 50,000 schools.<br>Impact is a core pillar of the education reform contributions from both partners, from improving student, teacher and school performance, through to improving university reform in short periods of time......</p>
  </section>
  <div class="abs btn-work">Read More</div>

  <footer class="abs footer">
    <h4 style="left:66px">Quick Links</h4>
    <ul>
      <li>Home</li><li>About Us</li><li>Services</li><li>Study Abroad</li><li>Test Preparation</li><li>News &amp; Event</li><li>Contact US</li><li>Gallery</li>
    </ul>
    <h4 style="left:350px">Address</h4>
    <div class="addr">Business Center<br>Marwan Crest Building,<br>Harbor Free Zone,<br>Qasr Al Noor, U.A.E.</div>
    <h4 style="left:626px">Contact Us</h4>
    <div class="btn-contact">CONTCT</div>
  </footer>
  <div class="abs base"><span style="left:68px">© 2017 Copyright. All Rights Reserved.</span><span style="left:615px;top:27px">Developed by</span></div>
</div>
</body>
</html>
```